Aviation security consulting company needs a website

We need a website design for Brisk Holloway, and aviation security consulting company. Brisk Holloway (www.briskholloway.example) is an aviation security consulting company that works with government and industry stakeholders in over 60 countries on aviation security strategy, governance, and oversight at the regulatory and operational level.
Brisk Holloway is strongly internationally focused.
The website required should be simple, corporate, serious, and communicate professionalism, reliability and honesty. We are trying to give the company a feeling of being well established.
The attached files include the company logo, along with examples of company web page styles that we like.
The Brisk Holloway website need only be around five pages long (landing page, who we are, our services, our clients, contact), though don't feel limited to only five pages.
The existing website (www.briskholloway.example) was rushed and put together using Wix. We don't love the existing website as it looks too amateur, so don't use it as a template.
There is no requirement for any online sales tools to be included in the site. The site is purely informational, with the option of people making contact via email.

```html
<!DOCTYPE html>
<html lang="en">
<head>
<meta charset="utf-8">
<title>Brisk Holloway — Aviation Security Consulting</title>
<link href="https://fonts.googleapis.com/css2?family=Arimo:wght@400;700&display=swap" rel="stylesheet">
<style>
  :root {
    --navy: #0c1740;
    --sky-top: #b9d0de;
    --sky-mid: #dfe8ee;
    --cloud: #e9ebec;
    --haze: #c7d3db;
    --text-grey: #56616b;
    --muted-blue: #8ea4b8;
    --accent-red: #b3243a;
    --frame: #8aa0b0;
    --white: #ffffff;
    --arrow-left: #1a2a5c;
    --arrow-right: #8a99a6;
  }
  * { margin: 0; padding: 0; box-sizing: border-box; }
  html, body { width: 1200px; height: 900px; overflow: hidden; }
  body { font-family: "Arimo", Arial, sans-serif; background: var(--white); }
  .page { position: relative; width: 1200px; height: 900px; overflow: hidden; }

  .hero-photo {
    position: absolute; inset: 0;
    background:
      radial-gradient(ellipse 60% 30% at 55% 88%, var(--cloud) 0%, rgba(233,235,236,0) 70%),
      linear-gradient(180deg, var(--sky-top) 0%, var(--sky-mid) 45%, #efeeec 62%, var(--haze) 80%, var(--cloud) 100%);
  }
  .content-frame {
    position: absolute; left: 240px; top: 87px; width: 915px; height: 769px;
    border: 1px solid var(--frame);
  }
  .navy-panel { position: absolute; inset: 0; width: 1200px; height: 900px; }

  .brand { position: absolute; left: 55px; top: 45px; display: flex; align-items: center; gap: 9px; color: var(--white); }
  .brand-mark { width: 46px; height: 46px; border: 4px solid var(--white); }
  .brand-name { font-size: 24px; font-weight: 700; letter-spacing: -0.5px; line-height: 1; }
  .brand-tagline { font-size: 10.5px; letter-spacing: 1.6px; margin-top: 1px; }

  .main-nav { position: absolute; top: 42px; right: 72px; display: flex; gap: 30px; align-items: center; }
  .main-nav a { color: var(--text-grey); text-decoration: none; font-size: 14px; padding-bottom: 3px; }
  .main-nav a.is-active { color: var(--navy); border-bottom: 2px solid var(--accent-red); }
  .menu-toggle { position: absolute; top: 44px; right: 54px; width: 15px; }
  .menu-toggle span { display: block; height: 1.5px; background: var(--navy); margin-bottom: 2.5px; }

  .about { position: absolute; left: 676px; top: 250px; width: 400px; }
  .about-label { color: var(--muted-blue); font-size: 20px; }
  .about-title { color: var(--navy); font-size: 38px; font-weight: 400; margin-top: 20px; line-height: 1; }
  .about-rule { width: 88px; height: 3px; background: var(--accent-red); margin: 16px 0 13px 2px; }
  .about-text { color: var(--text-grey); font-size: 20.5px; line-height: 22.5px; }
  .about-text + .about-text { margin-top: 21px; }
  .btn-services {
    display: inline-block; margin-top: 41px; padding: 10px 13px;
    border: 2px solid var(--navy); color: var(--navy); font-size: 21px; text-decoration: none;
    background: rgba(255,255,255,0.15);
  }

  .slide-arrow { position: absolute; top: 398px; width: 104px; height: 104px; border-radius: 50%; }
  .slide-arrow.prev { left: -52px; background: var(--arrow-left); }
  .slide-arrow.next { left: 1148px; background: var(--arrow-right); }
  .slide-arrow svg { position: absolute; top: 37px; }
  .slide-arrow.prev svg { left: 55px; }
  .slide-arrow.next svg { left: 8px; }

  .social-links { position: absolute; left: 53px; top: 836px; display: flex; gap: 16px; }
  .social-links a { color: var(--white); font-size: 14px; font-weight: 700; text-decoration: none; }

  .copyright { position: absolute; right: 45px; top: 871px; color: var(--muted-blue); font-size: 14px; }
</style>
</head>
<body>
<div class="page">
  <div class="hero-photo" role="img" aria-label="Photograph of a white passenger jet banking above a sea of clouds in a pale blue sky"></div>
  <div class="content-frame"></div>

  <svg class="navy-panel" viewBox="0 0 1200 900" aria-hidden="true">
    <polygon points="0,0 547,0 227,900 0,900" fill="var(--navy)"/>
  </svg>

  <header>
    <div class="brand">
      <div class="brand-mark"></div>
      <div>
        <div class="brand-name">Brisk Holloway</div>
        <div class="brand-tagline">aviation security consulting</div>
      </div>
    </div>
    <nav class="main-nav">
      <a href="#" class="is-active">HOME</a>
      <a href="#">OUR CLIENTS</a>
      <a href="#">CONTACTS</a>
    </nav>
    <div class="menu-toggle"><span></span><span></span><span></span><span></span></div>
  </header>

  <section class="about">
    <div class="about-label">ABOUT US</div>
    <h1 class="about-title">BRISK HOLLOWAY</h1>
    <div class="about-rule"></div>
    <p class="about-text">is a full service aviation security consulting company with experience in over 60 countries. We work with government and industry stakeholders to deliver outstanding security outcomes at both a regulatory and operational level.</p>
    <p class="about-text">Contact us to discuss your aviation security requirements and how we can work in partnership to ensure you exceed your domestic and international aviation security obligations.</p>
    <a href="#" class="btn-services">OUR SERVICES</a>
  </section>

  <a href="#" class="slide-arrow prev" aria-label="Previous">
    <svg width="40" height="30" viewBox="0 0 40 30"><path d="M38 15H3M16 2L3 15l13 13" fill="none" stroke="#9fb0cc" stroke-width="1.6"/></svg>
  </a>
  <a href="#" class="slide-arrow next" aria-label="Next">
    <svg width="40" height="30" viewBox="0 0 40 30"><path d="M2 15h35M24 2l13 13-13 13" fill="none" stroke="#ffffff" stroke-width="1.6"/></svg>
  </a>

  <nav class="social-links">
    <a href="#">Facet</a>
    <a href="#">Chirp</a>
    <a href="#">Reel</a>
  </nav>

  <footer class="copyright">© 2016 BRISK HOLLOWAY</footer>
</div>
</body>
</html>
```